Counseling Practice Business Card

I need a professional looking business card incorporating my new logo that was just completed. Card needs to incorporate my name and title, description of my specialty, my address, my phone number, my fax number, my email and my website URL. I need to be able to choose design on/with different paper colors and textures.
I do not have a lot of business card ideas so I am open to anything but I want bold,sharp, clear card without additional designs other than my logo (see attached file info). I am open to different color backgrounds or paper colors including black. I do not like traditional brackets around area codes in phone number or dashes between numbers in phone number. Am open to other ways of presenting including periods between numbers as appropriate. I do not know enough to know what I like yet but I want card to coordinate and work together with my logo. My practice emphasizes natural mental health interventions so any use of color (with background paper color or the blue and green in my logo) that elicits nature is nice. In addition to black, any natural brown or wood looking background might be desirable also. Most of the offerings so far look very similar and boring.

Target Market(s)

Potential therapy clients and other professionals

Contact Information for Business Card

Card information:
Marcus T. Whitfield, Ph.D.
Licensed Clinical Psychologist
Integrative Health Coach
4812 Ferndale Pkwy NW
Suite 730
Duluth, GA 30096
(770) 555-0142 phone
(770) 555-0186 fax
drmarcuswhitfield@kelvora.com
pathbloomcounseling.com

Font styles to use
Serif
Sans Serif
Other font styles liked:
• anything that you think looks crisp, clear and easily readable

Requirements
Must have
• Any color used should coordinate with my logo design (see attached files).
• Card should be printed horizontally so top and bottom are longest sides of rectangle.
• Background color or paper color should complement and highlight logo. Do not like a white background. black, grey, brown or any color my logo would blend well with.
Nice to have
• I would like designer to utilize color to highlight letters/name or phone-fax-web symbols.
• Bottom edge of card could be highlighted if appropriate to an idea.
Should not have
• I would NOT want the card to have a pure white background at all.
• No clear cards.
• Cards should be oriented with long sides on bottom and top, NOT sides. DO NOT LIKE THIS THIN TALL ORIENTATION.

```html
<!DOCTYPE html>
<html lang="en">
<head>
<meta charset="utf-8">
<title>Pathbloom Counseling – Business Card</title>
<link rel="stylesheet" href="https://fonts.googleapis.com/css2?family=Source+Sans+3:wght@400;600;700&display=swap">
<style>
  :root {
    --backdrop: #d9d0c0;
    --card: #141516;
    --card-edge: #222426;
    --brand-blue: #2a7fc4;
    --brand-green: #1f8a4a;
    --text-light: #dcdcdc;
    --text-muted: #bfc2c4;
    --divider: #5a5e62;
  }
  * { box-sizing: border-box; margin: 0; padding: 0; }
  html, body { width: 1200px; height: 840px; overflow: hidden; }
  body {
    background: var(--backdrop);
    font-family: "Source Sans 3", "Helvetica Neue", Arial, sans-serif;
    position: relative;
  }
  .card {
    position: absolute;
    left: 290px;
    width: 620px;
    height: 354px;
    background: var(--card);
    border: 1px solid var(--card-edge);
    box-shadow: 0 10px 24px rgba(0,0,0,0.28);
  }
  .card--front { top: 48px; }
  .card--back { top: 438px; }

  .brand {
    display: flex;
    align-items: center;
    gap: 12px;
    color: var(--brand-blue);
    font-weight: 700;
    white-space: nowrap;
  }
  .brand__name { display: block; line-height: 0.95; }
  .brand__line { display: block; }
  .brand__dot {
    width: 22px; height: 22px;
    border-radius: 50%;
    background: var(--brand-green);
    flex: none;
  }
  .card--front .brand {
    position: absolute;
    left: 0; right: 0; top: 96px;
    justify-content: center;
    font-size: 42px;
  }
  .front__url {
    position: absolute;
    left: 0; right: 0; top: 262px;
    text-align: center;
    color: var(--text-muted);
    font-size: 17px;
    letter-spacing: 4px;
  }

  .card--back .brand {
    position: absolute;
    left: 60px; top: 168px;
    font-size: 32px;
    gap: 10px;
  }
  .card--back .brand__dot { width: 17px; height: 17px; }
  .back__divider {
    position: absolute;
    left: 300px; top: 40px;
    width: 1px; height: 280px;
    background: linear-gradient(to bottom, var(--divider), rgba(90,94,98,0));
  }
  .back__accent {
    position: absolute;
    left: 297px; top: 44px;
    width: 7px; height: 40px;
    background: linear-gradient(to bottom, var(--brand-green) 0 50%, var(--brand-blue) 50% 100%);
  }
  .details {
    position: absolute;
    left: 318px; top: 38px;
    right: 16px;
    line-height: 1.22;
  }
  .details__name {
    color: var(--brand-blue);
    font-weight: 700;
    font-size: 20px;
    text-transform: uppercase;
    letter-spacing: 0.2px;
  }
  .details__title {
    color: var(--brand-green);
    font-size: 17px;
  }
  .details__address {
    margin-top: 12px;
    color: var(--text-light);
    font-size: 17px;
    font-style: normal;
  }
  .contacts {
    list-style: none;
    margin-top: 8px;
    color: var(--text-light);
    font-size: 16px;
  }
  .contacts li {
    display: flex;
    align-items: center;
    gap: 9px;
    height: 22px;
  }
  .contacts svg { width: 14px; height: 14px; flex: none; fill: var(--brand-blue); }
</style>
</head>
<body>

<section class="card card--front" aria-label="Card front">
  <div class="brand"><span class="brand__dot"></span><span class="brand__name"><span class="brand__line">Pathbloom</span><span class="brand__line">Counseling</span></span></div>
  <p class="front__url">www.pathbloomcounseling.com</p>
</section>

<section class="card card--back" aria-label="Card back">
  <div class="brand"><span class="brand__dot"></span><span class="brand__name"><span class="brand__line">Pathbloom</span><span class="brand__line">Counseling</span></span></div>
  <div class="back__divider"></div>
  <div class="back__accent"></div>
  <div class="details">
    <p class="details__name">Marcus T. Whitfield, Ph.D.</p>
    <p class="details__title">Licensed Clinical Psychologist</p>
    <p class="details__title">Integrative Health Coach</p>
    <address class="details__address">4812 Ferndale Pkwy NW<br>Suite 730<br>Duluth, GA 30096</address>
    <ul class="contacts">
      <li>
        <svg viewBox="0 0 16 16" aria-hidden="true"><path d="M3.6 1.2l2.3 2.8-1.3 1.6c.9 2 2.6 3.7 4.6 4.6l1.6-1.3 2.8 2.3-1.3 2.4C7.5 13.9 2.1 8.5 1.2 3.2z"/></svg>
        <span>(770) 555-0142</span>
      </li>
      <li>
        <svg viewBox="0 0 16 16" aria-hidden="true"><path d="M4 1h8v4H4zM2 6h12a1 1 0 0 1 1 1v5h-3v3H4v-3H1V7a1 1 0 0 1 1-1zm3 5v3h6v-3z"/></svg>
        <span>(770) 555-0186</span>
      </li>
      <li>
        <svg viewBox="0 0 16 16" aria-hidden="true"><path d="M1 3h14v10H1zm1.5 1.2V5l5.5 4 5.5-4v-.8z"/></svg>
        <span>drmarcuswhitfield@kelvora.com</span>
      </li>
      <li>
        <svg viewBox="0 0 16 16" aria-hidden="true"><circle cx="8" cy="8" r="7"/><path d="M1 8h14M8 1c2.5 2 2.5 12 0 14M8 1c-2.5 2-2.5 12 0 14" stroke="#141516" stroke-width="1.1" fill="none"/></svg>
        <span>www.pathbloomcounseling.com</span>
      </li>
    </ul>
  </div>
</section>

</body>
</html>
```